Glen Holbrook Announces his new career move! 8x5 card please.

Associate Broker GLEN HOLBROOK is proud to announce his new affiliation with m.vorlund bayshore estates, ltd.

His goal remains to meet all your real estate needs. Prepare to renew your seasonal rental for 2016...with the full support of his new office, Glen can handle your renewal seamlessly.

Prepared to purchase? With access to every property on the market...Glen can show you how easy it making your summer dreams come true can be.

Thinking about selling? m.vorlund bayshore estates, ltd. now offers the benefits of the Multiple Listing Service (MLS) to all sellers. In cooperation with MLS Sellers receive the maximum worldwide exposure, Purchasers receive a larger volume of properties to view and in cooperation with other Realtors, the transaction is handled professionally!!!!

I will send logo and photo of Glen Holbrook separately. Thank you. P-
Updates

Target Market(s)

Tenants, Sellers & Buyers

Industry/Entity Type

Broker

Font styles to use
Sans Serif

Requirements
Must have
• I attached logo and photo of Glen. Added a better photo of Glen.
Nice to have
• A photo of a property we have listed. I added a couple to choose from.
Should not have
• No Red color

```html
<!DOCTYPE html>
<html lang="en">
<head>
<meta charset="utf-8">
<title>Glen Holbrook – m.vorlund bayshore estates, ltd. postcard</title>
<link rel="stylesheet" href="https://fonts.googleapis.com/css2?family=Open+Sans:wght@400;600;700;800&family=Teko:wght@400;500&display=swap">
<style>
  :root {
    --stage: #d9d9d9;
    --paper: #ffffff;
    --sky-light: #f1f1f1;
    --sky-mid: #d4d4d4;
    --slate-dark: #3f3f41;
    --slate-mid: #6a6a6c;
    --slate-light: #8a8a8c;
    --sage: #8fb59b;
    --teal: #7ecdb5;
    --orange: #f0892a;
    --ink: #3a3a3a;
    --band: #d6d6d6;
    --white: #ffffff;
  }
  * { box-sizing: border-box; margin: 0; padding: 0; }
  html, body { width: 900px; height: 1200px; overflow: hidden; }
  body {
    background: var(--stage);
    font-family: "Open Sans", Arial, sans-serif;
    position: relative;
  }
  .card {
    position: absolute;
    overflow: hidden;
    background: var(--paper);
    box-shadow: 0 4px 14px rgba(0,0,0,.25);
  }

  /* ---------- front ---------- */
  .card-front { left: 78px; top: 45px; width: 744px; height: 530px; }
  .front-art { position: absolute; inset: 0; }
  .brand-name {
    position: absolute; left: 28px; top: 22px;
    font-weight: 700; font-size: 34px; letter-spacing: -1px;
    color: var(--ink);
  }
  .offer-purchase {
    position: absolute; right: 20px; top: 242px; width: 360px;
    text-align: right; color: var(--white);
  }
  .offer-purchase .kicker {
    font-family: "Teko", "Arial Narrow", sans-serif;
    font-size: 30px; line-height: 28px; color: var(--orange); letter-spacing: .5px;
  }
  .offer-purchase .lead { font-weight: 700; font-size: 18px; line-height: 22px; }
  .offer-purchase .detail { font-size: 18px; line-height: 22px; }
  .offer-renew {
    position: absolute; left: 22px; top: 400px; color: var(--white);
  }
  .offer-renew .headline {
    font-weight: 700; font-size: 24px; color: var(--orange); line-height: 32px;
  }
  .offer-renew .detail { font-size: 16.5px; line-height: 22px; }
  .front-url {
    position: absolute; left: 0; right: 0; top: 472px; height: 34px;
    text-align: center; line-height: 34px;
    font-weight: 700; font-size: 18px; letter-spacing: 3.5px; color: var(--slate-dark);
  }

  /* ---------- back ---------- */
  .card-back { left: 78px; top: 622px; width: 747px; height: 533px; }
  .message-side {
    position: absolute; left: 0; top: 0; width: 434px; height: 100%;
    background: linear-gradient(90deg, var(--slate-dark) 0%, var(--slate-mid) 55%, var(--slate-light) 100%);
  }
  .interior-photo {
    position: absolute; left: 120px; top: 0; width: 314px; height: 300px;
    background: radial-gradient(ellipse at 60% 45%, rgba(220,220,215,.35), rgba(120,120,120,0) 70%);
  }
  .sell-heading {
    position: absolute; left: 27px; top: 36px;
    font-family: "Teko", "Arial Narrow", sans-serif; font-weight: 500;
    font-size: 72px; line-height: 58px; color: var(--orange);
  }
  .sell-copy {
    position: absolute; left: 27px; top: 200px; width: 385px;
    color: var(--white); font-size: 17px; line-height: 19px;
  }
  .sell-copy p + p { margin-top: 19px; }
  .call-button {
    position: absolute; left: 0; top: 420px; width: 288px; height: 52px;
    background: var(--teal); border-radius: 0 10px 10px 0;
    display: flex; align-items: center; padding-left: 12px; gap: 2px;
    color: var(--white); font-weight: 700; font-size: 23px;
  }
  .call-button svg { width: 26px; height: 26px; }
  .back-url {
    position: absolute; left: 0; width: 434px; top: 490px;
    text-align: center; color: var(--white); font-weight: 700; font-size: 15px;
  }
  .address-side { position: absolute; left: 434px; top: 0; right: 0; bottom: 0; background: var(--paper); }
  .stamp-box {
    position: absolute; left: 188px; top: 88px; width: 62px; height: 78px;
    border: 2px solid #111;
  }
  .address-line {
    position: absolute; left: 36px; width: 212px; height: 0; border-top: 2px solid #111;
  }
</style>
</head>
<body>

<section class="card card-front" aria-label="Postcard front">
  <svg class="front-art" width="744" height="530" viewBox="0 0 744 530">
    <defs>
      <linearGradient id="skyFade" x1="0" y1="0" x2="0" y2="1">
        <stop offset="0" stop-color="#f4f4f4"/>
        <stop offset="1" stop-color="#d8d8d8"/>
      </linearGradient>
      <linearGradient id="slateBody" x1="0" y1="0" x2="1" y2="0">
        <stop offset="0" stop-color="#59595b"/>
        <stop offset="0.6" stop-color="#4a4a4c"/>
        <stop offset="1" stop-color="#6c6c6e"/>
      </linearGradient>
      <linearGradient id="bandFade" x1="0" y1="0" x2="1" y2="0">
        <stop offset="0" stop-color="#c9c9c9"/>
        <stop offset="0.5" stop-color="#e2e2e2"/>
        <stop offset="1" stop-color="#c9c9c9"/>
      </linearGradient>
      <clipPath id="bedClip"><circle cx="127" cy="240" r="90"/></clipPath>
      <clipPath id="loungeClip"><circle cx="284" cy="295" r="74"/></clipPath>
    </defs>
    <rect class="beach-house-photo" width="744" height="260" fill="url(#skyFade)" role="img" aria-label="Faded photo of a beach house exterior"/>
    <path class="wave-sage" d="M0,205 C150,165 300,140 430,175 C560,210 650,190 744,150 L744,530 L0,530 Z" fill="var(--sage)"/>
    <path class="wave-white" d="M0,218 C150,178 300,153 430,188 C560,223 650,203 744,163 L744,530 L0,530 Z" fill="#f2f2f2"/>
    <path class="wave-slate" d="M0,224 C150,184 300,159 430,194 C560,229 650,209 744,169 L744,530 L0,530 Z" fill="url(#slateBody)"/>
    <circle cx="127" cy="240" r="95" fill="var(--sage)"/>
    <rect clip-path="url(#bedClip)" x="37" y="150" width="180" height="180" fill="#cfd3d6" role="img" aria-label="Photo of a bright bedroom with white bedding"/>
    <circle cx="284" cy="295" r="79" fill="#3a3a3c"/>
    <rect clip-path="url(#loungeClip)" x="210" y="221" width="148" height="148" fill="#b9bcc4" role="img" aria-label="Photo of a living room with a grey sofa"/>
    <rect x="0" y="472" width="744" height="34" fill="url(#bandFade)"/>
    <rect x="0" y="506" width="744" height="24" fill="#444446"/>
  </svg>

  <div class="brand-name">m.vorlund bayshore estates, ltd.</div>

  <div class="offer-purchase">
    <p class="kicker">PREPARED TO PURCHASE?</p>
    <p class="lead">With access to every property on the market...</p>
    <p class="detail">Glen can show you how easy it making your summer dreams come true can be.</p>
  </div>

  <div class="offer-renew">
    <p class="headline">Prepare to renew your seasonal rental for 2016...</p>
    <p class="detail">with the full support of his new office, Glen can handle your renewal seamlessly</p>
  </div>

  <div class="front-url">www.bayshorepines.com</div>
</section>

<section class="card card-back" aria-label="Postcard back">
  <div class="message-side">
    <div class="interior-photo" role="img" aria-label="Faded photo of a dining room interior"></div>
    <h2 class="sell-heading">THINKING ABOUT<br>SELLING?</h2>
    <div class="sell-copy">
      <p>m.vorlund bayshore estates, ltd. now offers the benefits of the Multiple Listing Service (MLS) to all sellers.</p>
      <p>In cooperation with MLS Sellers receive the maximum worldwide exposure, Purchasers receive a larger volume of properties to view and in cooperation with other Realtors, the transaction is handled professionally!!!!</p>
    </div>
    <div class="call-button">
      <svg viewBox="0 0 24 24" aria-hidden="true"><path fill="#ffffff" d="M6.6 10.8c1.4 2.8 3.8 5.1 6.6 6.6l2.2-2.2c.3-.3.7-.4 1-.2 1.1.4 2.3.6 3.6.6.6 0 1 .4 1 1V20c0 .6-.4 1-1 1C10.6 21 3 13.4 3 4c0-.6.4-1 1-1h3.5c.6 0 1 .4 1 1 0 1.3.2 2.5.6 3.6.1.3 0 .7-.2 1L6.6 10.8z"/></svg>
      <span>CALL- 555-014-2290</span>
    </div>
    <div class="back-url">www.bayshoreestates.com</div>
  </div>
  <div class="address-side">
    <div class="stamp-box"></div>
    <div class="address-line" style="top:258px"></div>
    <div class="address-line" style="top:308px"></div>
    <div class="address-line" style="top:358px"></div>
    <div class="address-line" style="top:408px"></div>
  </div>
</section>

</body>
</html>
```